A Leisure SPA Plaza Hotel needs Creative VIP Cards Design

We need VIP Cards Design for a SPA Plaza Hotel, This leisure SPA plaza hotel have multiple sub projects, such as leisure hotel room, large buffet restaurant, swimming pool, theatrical performances, sauna bath, massage, SPA, Tea bar, 3D cinema, KTV rooms, chess room, Internet cafes , art appreciation, children's Castle, Korean geothermal, table tennis, billiard room, GYM and other entertainments.
We need Three creative VIP Card design for 3 different level:
1. Golden Card
2. Platinum Card
3. Diamond Card
Attached, Please find the LOGO file and some sample, we new design with much better look than those samples.

```html
<!DOCTYPE html>
<html lang="zh">
<head>
<meta charset="utf-8">
<title>Pine Ridge Spa Resort — VIP Cards</title>
<link href="https://fonts.googleapis.com/css2?family=Playfair+Display:wght@700&family=Noto+Sans+SC:wght@400&display=swap" rel="stylesheet">
<style>
  :root {
    --backdrop: #dcdcdc;
    --card-black: #141414;
    --ink-white: #f4f4f4;
    --ink-muted: #cfcfcf;
    --gold-light: #ffe27a;
    --gold-mid: #e8b52a;
    --gold-deep: #9c6a0c;
    --silver-light: #f7f7f7;
    --silver-mid: #bdbdbd;
    --silver-deep: #7c7c7c;
    --diamond-light: #ffffff;
    --diamond-mid: #dcdcdc;
    --diamond-deep: #a9a9a9;
  }
  * { box-sizing: border-box; margin: 0; padding: 0; }
  html, body {
    width: 1200px; height: 864px; overflow: hidden;
    background: var(--backdrop);
  }
  .card-set { position: relative; width: 1200px; height: 864px; }
  .card {
    position: absolute; width: 520px; height: 320px;
    border-radius: 14px; overflow: hidden;
    background: var(--card-black);
    box-shadow: 0 10px 24px rgba(0,0,0,.28);
  }
  .card--gold { left: 340px; top: 70px; }
  .card--platinum { left: 50px; top: 470px; }
  .card--diamond { left: 630px; top: 470px; }
  .card__face { position: absolute; inset: 0; width: 100%; height: 100%; }
  .brand {
    position: absolute; right: 34px; top: 70px;
    display: flex; align-items: center; gap: 10px;
    font-family: "Noto Sans SC", sans-serif; font-weight: 400;
    color: var(--ink-white);
  }
  .brand__mark { width: 14px; height: 14px; border-radius: 50%; background: var(--ink-white); flex: none; }
  .brand__name { line-height: 1.25; text-align: right; }
  .brand__name-cn { display: block; font-size: 24px; letter-spacing: 1px; }
  .brand__name-en { display: block; font-size: 13px; }
  .card-no {
    position: absolute; right: 34px; top: 136px;
    font-family: "Noto Sans SC", sans-serif; font-size: 11px;
    color: var(--ink-muted); letter-spacing: 1px;
  }
  .tier-vip {
    position: absolute; right: 34px; top: 152px;
    font-family: "Playfair Display", serif; font-weight: 700;
    font-size: 92px; line-height: 1;
    -webkit-background-clip: text; background-clip: text; color: transparent;
  }
  .card--gold .tier-vip { background-image: linear-gradient(180deg, var(--gold-light), var(--gold-mid) 55%, var(--gold-deep)); }
  .card--platinum .tier-vip,
  .card--diamond .tier-vip { background-image: linear-gradient(180deg, var(--silver-light), var(--silver-mid) 55%, var(--silver-deep)); }
  .tier-label {
    position: absolute; right: 40px; top: 262px;
    font-family: "Noto Sans SC", sans-serif; font-size: 15px;
    color: var(--ink-white); letter-spacing: 3px;
  }
</style>
</head>
<body>
<main class="card-set">

  <article class="card card--gold">
    <svg class="card__face" viewBox="0 0 520 320" aria-hidden="true">
      <defs>
        <linearGradient id="gold-foil" x1="0" y1="0" x2="1" y2="1">
          <stop offset="0" stop-color="var(--gold-light)"/>
          <stop offset=".5" stop-color="var(--gold-mid)"/>
          <stop offset="1" stop-color="var(--gold-deep)"/>
        </linearGradient>
      </defs>
      <path d="M0 0 H300 C250 50 250 140 200 200 C155 255 90 285 0 305 Z" fill="url(#gold-foil)" role="img" aria-label="Gold glitter panel with embossed swirl ornament"/>
      <path d="M308 2 C324 20 320 40 304 56" fill="none" stroke="var(--gold-mid)" stroke-width="3"/>
    </svg>
    <div class="brand"><span class="brand__mark"></span><span class="brand__name"><span class="brand__name-cn">松岚度假会所</span><span class="brand__name-en">Pine Ridge Spa Resort</span></span></div>
    <p class="card-no">NO. 000000000</p>
    <p class="tier-vip">VIP</p>
    <p class="tier-label">黄金会员卡</p>
  </article>

  <article class="card card--platinum">
    <svg class="card__face" viewBox="0 0 520 320" aria-hidden="true">
      <defs>
        <linearGradient id="diamond-facets" x1="0" y1="0" x2="1" y2="1">
          <stop offset="0" stop-color="var(--diamond-light)"/>
          <stop offset=".5" stop-color="var(--diamond-mid)"/>
          <stop offset="1" stop-color="var(--diamond-deep)"/>
        </linearGradient>
      </defs>
      <path d="M0 0 H300 C250 50 250 140 200 200 C155 255 90 285 0 305 Z" fill="url(#diamond-facets)" role="img" aria-label="Faceted diamond panel with embossed swirl ornament"/>
      <path d="M308 2 C324 20 320 40 304 56" fill="none" stroke="var(--silver-mid)" stroke-width="3"/>
    </svg>
    <div class="brand"><span class="brand__mark"></span><span class="brand__name"><span class="brand__name-cn">松岚度假会所</span><span class="brand__name-en">Pine Ridge Spa Resort</span></span></div>
    <p class="card-no">NO. 000000000</p>
    <p class="tier-vip">VIP</p>
    <p class="tier-label">钻石会员卡</p>
  </article>

  <article class="card card--diamond">
    <svg class="card__face" viewBox="0 0 520 320" aria-hidden="true">
      <defs>
        <linearGradient id="silver-foil" x1="0" y1="0" x2="1" y2="1">
          <stop offset="0" stop-color="var(--silver-light)"/>
          <stop offset=".5" stop-color="var(--silver-mid)"/>
          <stop offset="1" stop-color="var(--silver-deep)"/>
        </linearGradient>
      </defs>
      <path d="M0 0 H300 C250 50 250 140 200 200 C155 255 90 285 0 305 Z" fill="url(#silver-foil)" role="img" aria-label="Silver glitter panel with embossed swirl ornament"/>
      <path d="M308 2 C324 20 320 40 304 56" fill="none" stroke="var(--silver-mid)" stroke-width="3"/>
    </svg>
    <div class="brand"><span class="brand__mark"></span><span class="brand__name"><span class="brand__name-cn">松岚度假会所</span><span class="brand__name-en">Pine Ridge Spa Resort</span></span></div>
    <p class="card-no">NO. 000000000</p>
    <p class="tier-vip">VIP</p>
    <p class="tier-label">铂金会员卡</p>
  </article>

</main>
</body>
</html>
```